Business card for auto dealership

Looking for a clean modern design.
Would like attached logo incorporated

Industry/Entity Type

Car dealership

Contact Information for Business Card

Name, website, phone, cell, fax, email

```html
<!DOCTYPE html>
<html lang="en">
<head>
<meta charset="utf-8">
<title>Halloway Truck &amp; Auto Sales – Business Card</title>
<link rel="stylesheet" href="https://fonts.googleapis.com/css2?family=Source+Serif+4:wght@300;400;700&family=Roboto:wght@400&display=swap">
<style>
  :root {
    --gold-dark: #8e7050;
    --gold-mid: #c4a073;
    --gold-light: #ebc486;
    --black: #000000;
    --white: #ffffff;
    --pattern-white: #f9f9f9;
    --muted: #b9b9b9;
  }
  * { margin: 0; padding: 0; box-sizing: border-box; }
  html, body { width: 1200px; height: 996px; overflow: hidden; background: var(--white); }
  body { position: relative; font-family: "Source Serif 4", Georgia, serif; }

  /* Card back */
  .card-back { position: absolute; left: 0; top: 0; width: 1200px; height: 465px; }
  .card-back .surface {
    position: absolute; inset: 0;
    background: linear-gradient(90deg, var(--gold-dark) 0%, var(--gold-mid) 50%, var(--gold-light) 100%);
  }
  .card-back .tab {
    position: absolute; left: 495px; top: 0; width: 211px; height: 24px;
    background: var(--black); border-radius: 0 0 10px 10px;
  }
  .wordmark { position: absolute; text-align: center; color: var(--black); font-weight: 700; line-height: 1; }
  .card-back .wordmark { left: 0; width: 1200px; top: 168px; font-size: 58px; }
  .wordmark .sub { display: block; font-size: 0.36em; margin-top: 8px; letter-spacing: 0.04em; }
  .card-back .web-band {
    position: absolute; left: 0; top: 371px; width: 1200px; height: 38px;
    background: var(--black); color: var(--white);
    font-family: "Roboto", Arial, sans-serif; font-size: 14px;
    display: flex; align-items: center; justify-content: center;
  }

  /* Card front */
  .card-front { position: absolute; left: 0; top: 465px; width: 1200px; height: 531px; background: var(--pattern-white); }
  .card-front .info-panel { position: absolute; left: 0; top: 0; width: 560px; height: 531px; background: var(--black); }
  .card-front .accent {
    position: absolute; left: 560px; top: 0; width: 170px; height: 531px;
    background: linear-gradient(90deg, var(--gold-dark) 0%, var(--gold-light) 100%);
  }
  .card-front .wordmark { left: 800px; width: 310px; top: 225px; font-size: 40px; }
  .card-front .wordmark .sub { margin-top: 6px; }

  .name { position: absolute; left: 150px; top: 62px; color: var(--white); font-size: 32px; font-weight: 700; letter-spacing: 0.01em; }
  .role { position: absolute; left: 157px; top: 102px; color: var(--muted); font-size: 20px; font-weight: 300; }

  .contact { position: absolute; left: 130px; display: flex; align-items: center; color: var(--white); }
  .contact .icon { width: 48px; height: 48px; flex: none; }
  .contact .text { margin-left: 22px; font-size: 24px; line-height: 30px; }
  .contact .text.bold { font-weight: 700; }
  .contact-web { top: 178px; }
  .contact-phone { top: 288px; align-items: flex-start; }
  .contact-mail { top: 438px; }
  .divider { position: absolute; left: 200px; width: 98px; height: 2px; background: linear-gradient(90deg, var(--gold-mid), var(--gold-light)); }
</style>
</head>
<body>

<section class="card-back">
  <div class="surface" role="img" aria-label="Gold gradient background with faint hexagon pattern"></div>
  <div class="tab"></div>
  <div class="wordmark">Halloway<span class="sub">TRUCK &amp; AUTO SALES</span></div>
  <div class="web-band">Hallowayauto.com</div>
</section>

<section class="card-front">
  <svg width="0" height="0" style="position:absolute">
    <defs>
      <linearGradient id="iconGold" x1="0" y1="0" x2="1" y2="0">
        <stop offset="0" stop-color="#8e7050"/><stop offset="1" stop-color="#ebc486"/>
      </linearGradient>
    </defs>
  </svg>

  <div class="info-panel"></div>
  <div class="accent" role="img" aria-label="Gold faceted decoration dividing the dark and light halves"></div>

  <div class="name">JORDAN HALLOWAY</div>
  <div class="role">Car dealership</div>

  <div class="contact contact-web">
    <svg class="icon" viewBox="0 0 48 48">
      <circle cx="24" cy="24" r="24" fill="url(#iconGold)"/>
      <g fill="none" stroke="#fff" stroke-width="1.6">
        <circle cx="24" cy="24" r="12"/>
        <ellipse cx="24" cy="24" rx="5.5" ry="12"/>
        <line x1="12" y1="24" x2="36" y2="24"/>
        <line x1="14" y1="18" x2="34" y2="18"/>
        <line x1="14" y1="30" x2="34" y2="30"/>
      </g>
    </svg>
    <span class="text bold">Hallowayauto.com</span>
  </div>

  <div class="divider" style="top:255px"></div>

  <div class="contact contact-phone">
    <svg class="icon" viewBox="0 0 48 48">
      <circle cx="24" cy="24" r="24" fill="#fff"/>
      <path d="M18 13c1.5-1 3 0 4 2l1.5 3c.6 1.3 0 2.3-1 3l-1 .8c.8 2.4 2.6 4.6 4.8 6l1-.9c1-.9 2-1.2 3.1-.4l2.8 2c1.6 1.2 1.6 2.8.3 4.1l-1.5 1.4c-2 1.8-6 .5-9.7-3.2-3.8-3.8-5.7-8.6-4.6-11.6z" fill="#b08f66"/>
    </svg>
    <span class="text">Office 555-310-4820<br>Cell 555-274-9163<br>Fax 555-386-5207</span>
  </div>

  <div class="divider" style="top:416px"></div>

  <div class="contact contact-mail">
    <svg class="icon" viewBox="0 0 48 48">
      <circle cx="24" cy="24" r="24" fill="url(#iconGold)"/>
      <rect x="11" y="15" width="26" height="18" fill="#fff"/>
      <polyline points="11,15 24,26 37,15" fill="none" stroke="#c4a073" stroke-width="1.4"/>
    </svg>
    <span class="text bold">jordan@hallowayauto.com</span>
  </div>

  <div class="wordmark">Halloway<span class="sub">TRUCK &amp; AUTO SALES</span></div>
</section>

</body>
</html>
```